Fern Hollow Academy business card

we need to incorporate our school logo, name, address onto a great new school business card for all our staff - I included a lot of detail below under must haves and I included 3 business card samples below also that give a flavour of what I want - I would like to include a great graphic on at least one side of the card that represents education -

Target Market(s)

this business card will need to be attractive to parents of all ages but especially millennial parents and even high school students who may influence parents to chose Fern Hollow Academy

Industry/Entity Type

Education

Contact Information for Business Card

should contain core value words "excellence service family belief"
will need out school name, Fern Hollow Academy to be present, address 7281 Tamsworth Road, Burnaby, British Columbia V3K1P8
telephone 604.719.2083 Ext. 317
first card will need my name on it, Morvena Pelchuk, Director of Development & Operations
also web address of fernhollowacademy.ca

Font styles to use
Other font styles liked:
• Tw Cent MT

Requirements
Must have
• a fresh modern look for a private school environment that appeals to parents looking for great education - must use school logo, and incorporate colours navy blue, CMYK 100, 60, 0, 56 and burgundy CMYK 27, 98, 81, 50
• below I uploaded 3 business card layouts that look interesting to me - I'd like to incorporate some great school photos into the design - I tried to upload some school photos that we have, that the files are too large apparently? so I could send a link to Filecrate or something like that to share great high res pics that would look nice - we are kindergarten to Gr. 12 school, so I would like to include images that would represent great education at any age.
Nice to have
• spot colour would be nice as an option for printing for maybe key administrator business cards, while the rest would be basic printing

```html
<!DOCTYPE html>
<html lang="en">
<head>
<meta charset="utf-8">
<title>Fern Hollow Academy – Business Card</title>
<link href="https://fonts.googleapis.com/css2?family=Questrial&display=swap" rel="stylesheet">
<style>
  :root {
    --navy: #0f3a6e;
    --navy-deep: #0b2d57;
    --burgundy: #7a1626;
    --white: #ffffff;
    --stage: #e9ebef;
    --card-font: "Questrial", sans-serif;
  }
  * { margin: 0; padding: 0; box-sizing: border-box; }
  html, body {
    width: 1200px; height: 900px; overflow: hidden;
    background: var(--stage);
    font-family: var(--card-font);
  }
  .canvas { position: relative; width: 1200px; height: 900px; }

  .card {
    position: absolute;
    width: 700px; height: 400px;
    border-radius: 22px;
    overflow: hidden;
    box-shadow: 0 10px 30px rgba(0,0,0,.18);
    color: var(--white);
  }

  /* Back: brand side */
  .card-brand { left: 250px; top: 35px; background: var(--navy); text-align: center; }
  .brand-mark {
    position: absolute; left: 0; right: 0; top: 95px;
    display: flex; align-items: center; justify-content: center; gap: 14px;
  }
  .brand-mark .dot { width: 18px; height: 18px; border-radius: 50%; background: var(--white); }
  .brand-mark .name { font-size: 38px; letter-spacing: .5px; }
  .brand-web { position: absolute; left: 0; right: 0; top: 280px; font-size: 20px; font-weight: 700; letter-spacing: .3px; }
  .brand-values { position: absolute; left: 0; right: 0; top: 318px; font-size: 24px; letter-spacing: 1px; }

  /* Front: contact side */
  .card-contact { left: 250px; top: 465px; }
  .card-contact .shapes { position: absolute; inset: 0; }
  .photo {
    position: absolute; inset: 0;
    background:
      radial-gradient(ellipse at 75% 60%, rgba(170,30,40,.55), transparent 55%),
      radial-gradient(ellipse at 55% 35%, rgba(200,160,130,.45), transparent 40%),
      linear-gradient(120deg, #5a4a44 0%, #231b1c 40%, #3a1417 70%, #1a1416 100%);
  }
  .photo-mark {
    position: absolute; left: 60px; top: 175px;
    display: flex; align-items: center; gap: 10px;
    font-size: 26px; color: rgba(255,255,255,.85);
  }
  .photo-mark .dot { width: 14px; height: 14px; border-radius: 50%; background: rgba(255,255,255,.85); }
  .person { position: absolute; right: 30px; top: 14px; text-align: center; width: 340px; }
  .person .name { font-size: 30px; letter-spacing: .5px; }
  .person .role { font-size: 15px; margin-top: 4px; }
  .address { position: absolute; right: 40px; top: 168px; text-align: right; font-size: 17px; line-height: 1.35; }
  .contact-list { position: absolute; right: 28px; top: 300px; list-style: none; text-align: right; font-size: 17px; line-height: 1.45; }
  .contact-list li { display: flex; justify-content: flex-end; align-items: center; gap: 10px; }
  .contact-list li.web { font-weight: 700; }
  .contact-list .icon { width: 13px; height: 13px; flex: none; }
</style>
</head>
<body>
<main class="canvas">

  <section class="card card-brand" aria-label="Business card back">
    <div class="brand-mark">
      <span class="dot"></span>
      <span class="name">Fern Hollow Academy</span>
    </div>
    <p class="brand-web">www.fernhollowacademy.ca</p>
    <p class="brand-values">EXCELLENCE SERVICE FAMILY BELIEF</p>
  </section>

  <section class="card card-contact" aria-label="Business card front">
    <div class="photo" role="img" aria-label="Photo of graduating students in caps and gowns"></div>
    <div class="photo-mark"><span class="dot"></span><span>Fern Hollow Academy</span></div>
    <svg class="shapes" viewBox="0 0 700 400" width="700" height="400" aria-hidden="true">
      <polygon points="345,0 700,0 700,95 320,95" fill="var(--navy)"/>
      <polyline points="320,95 345,0" stroke="var(--white)" stroke-width="4" fill="none"/>
      <polygon points="330,400 400,275 700,225 700,400" fill="var(--navy)"/>
      <polyline points="330,400 400,275 700,225" stroke="var(--white)" stroke-width="4" fill="none"/>
    </svg>
    <div class="person">
      <p class="name">Morvena Pelchuk</p>
      <p class="role">Director of Development &amp; Operations</p>
    </div>
    <p class="address">7281 Tamsworth Road, Burnaby<br>British Columbia V3K1P8</p>
    <ul class="contact-list">
      <li>604.719.2083 Ext. 317
        <svg class="icon" viewBox="0 0 24 24"><path d="M6 2l4 4-2 3c1 3 4 6 7 7l3-2 4 4-3 4C10 22 2 14 2 5z" fill="var(--white)"/></svg></li>
      <li>info@fernhollowacademy.ca
        <svg class="icon" viewBox="0 0 24 24"><rect x="2" y="5" width="20" height="14" fill="none" stroke="var(--white)" stroke-width="2"/><path d="M2 5l10 8 10-8" fill="none" stroke="var(--white)" stroke-width="2"/></svg></li>
      <li class="web">www.fernhollowacademy.ca
        <svg class="icon" viewBox="0 0 24 24"><circle cx="12" cy="12" r="10" fill="none" stroke="var(--white)" stroke-width="2"/><path d="M2 12h20M12 2c4 4 4 16 0 20M12 2c-4 4-4 16 0 20" fill="none" stroke="var(--white)" stroke-width="2"/></svg></li>
    </ul>
  </section>

</main>
</body>
</html>
```